Professional/modern business card design for construction company

We need a new business card design, double sided keeping it modern, sleek, professional and simple. We are an earthmoving business but do not want any pictures of machinery. I would like one side to have the logo and the other to have all the information, keeping with the colors in our logo. The business card will need to be able to be customised so we can use it for several different managers., we would also like to be able to use the design to apply it to other stationary ie. letterheads, notebooks etc. We do not really have a tag line but we could put on there that we specialise in - Agriculture, Civil Construction and Mining.

Contact Information for Business Card

Brolga Ridge Excavations Pty Ltd
ABN 58 402 937 615
82 Gumleaf Creek Road, Moree NSW 2400

Harold Benton
Managing Director
P 0418 639 204
E haroldbenton@brolgaridgeexc.com.au

Font styles to use
Serif
Sans Serif

Requirements
Nice to have
• I have attached some examples of ideas.
Should not have
• images of machinery

```html
<!DOCTYPE html>
<html lang="en">
<head>
<meta charset="utf-8">
<title>Brolga Ridge Excavations – Business Card</title>
<link rel="stylesheet" href="https://fonts.googleapis.com/css2?family=Open+Sans:wght@400;600;700&display=swap">
<style>
  :root {
    --orange: #f48b1f;
    --charcoal: #3f3f41;
    --text: #4a4a4a;
    --white: #ffffff;
    --backdrop: #2b2b2b;
  }
  * { margin: 0; padding: 0; box-sizing: border-box; }
  html, body { width: 1200px; height: 960px; overflow: hidden; }
  body {
    position: relative;
    background: var(--backdrop);
    font-family: "Open Sans", Arial, sans-serif;
  }
  .card {
    position: absolute;
    left: 261px;
    width: 679px;
    height: 388px;
  }
  .card--front { top: 61px; background: var(--white); }
  .card--back { top: 511px; background: var(--orange); }

  .front__brand {
    position: absolute;
    left: 300px; top: 210px;
    width: 250px;
    transform: translateX(-261px);
    color: var(--charcoal);
    font-weight: 700;
    text-align: center;
  }
  .front__brand-name { font-size: 36px; line-height: 40px; letter-spacing: 0.5px; }
  .front__brand-sub { font-size: 17px; line-height: 24px; letter-spacing: 0.4px; }

  .front__divider {
    position: absolute;
    left: 311px; top: 78px;
    width: 2px; height: 238px;
    background: linear-gradient(to bottom, rgba(60,60,60,0), rgba(60,60,60,0.75) 50%, rgba(60,60,60,0));
  }

  .contact { position: absolute; left: 339px; top: 80px; color: var(--text); font-size: 16px; line-height: 22px; }
  .contact__name { color: var(--orange); font-weight: 700; font-size: 23px; line-height: 28px; letter-spacing: 0.3px; }
  .contact__role { font-size: 17px; line-height: 24px; margin-bottom: 6px; color: #3a3a3a; }
  .contact__address { margin-bottom: 6px; }
  .contact__line { display: flex; align-items: center; gap: 6px; }
  .contact__line svg { width: 16px; height: 16px; flex: none; }
  .contact__abn { margin-top: 6px; }

  .front__rule { position: absolute; left: 0; right: 0; top: 369px; height: 3px; background: var(--charcoal); }
  .front__band { position: absolute; left: 0; right: 0; top: 374px; height: 14px; background: var(--orange); }

  .back__brand {
    position: absolute; left: 0; right: 0; top: 128px;
    text-align: center; color: var(--white); font-weight: 700;
  }
  .back__brand-name { font-size: 58px; line-height: 66px; letter-spacing: 1px; }
  .back__brand-sub { font-size: 24px; line-height: 34px; letter-spacing: 0.6px; }
  .back__tagline {
    position: absolute; left: 0; right: 0; top: 294px;
    text-align: center; color: var(--white); font-size: 16px; line-height: 23px;
  }
</style>
</head>
<body>
  <section class="card card--front">
    <div class="front__brand">
      <div class="front__brand-name">BROLGA RIDGE</div>
      <div class="front__brand-sub">EXCAVATIONS PTY LTD</div>
    </div>
    <div class="front__divider"></div>
    <div class="contact">
      <div class="contact__name">HAROLD BENTON</div>
      <div class="contact__role">Managing Director</div>
      <div class="contact__address">
        Brolga Ridge Excavations Pty Ltd<br>
        82 Gumleaf Creek Road<br>
        Moree NSW 2400
      </div>
      <div class="contact__line">
        <svg viewBox="0 0 16 16"><path fill="var(--orange)" d="M3 2h3l1.5 3.5-2 1.2a8 8 0 0 0 3.8 3.8l1.2-2L14 10v3a1 1 0 0 1-1 1A11 11 0 0 1 2 3a1 1 0 0 1 1-1z"/></svg>
        0418 639 204
      </div>
      <div class="contact__line">
        <svg viewBox="0 0 16 16"><rect x="1" y="3.5" width="14" height="9" rx="1" fill="var(--orange)"/><path d="M1.5 4l6.5 5 6.5-5" stroke="#fff" stroke-width="1.2" fill="none"/></svg>
        haroldbenton@brolgaridgeexc.com.au
      </div>
      <div class="contact__line">
        <svg viewBox="0 0 16 16"><circle cx="8" cy="8" r="7" fill="var(--orange)"/><path d="M1 8h14M8 1c3 3 3 11 0 14M8 1c-3 3-3 11 0 14" stroke="#fff" stroke-width="1" fill="none"/></svg>
        www.brolgaridgeexc.com.au
      </div>
      <div class="contact__abn">ABN 58 402 937 615</div>
    </div>
    <div class="front__rule"></div>
    <div class="front__band"></div>
  </section>

  <section class="card card--back">
    <div class="back__brand">
      <div class="back__brand-name">BROLGA RIDGE</div>
      <div class="back__brand-sub">EXCAVATIONS PTY LTD</div>
    </div>
    <p class="back__tagline">
      We specialise in<br>
      Agriculture, Civil Construction &amp; Mining.
    </p>
  </section>
</body>
</html>
```